Full service meeting planning company needs new business cards

Velmora Linkway is a full service meeting planning company that specializes in on-line conference registration web development and event communications. We combine citywide hotel management, mobile applications, eblast reminders, confirmation letters, and customized reporting to create a seamless registration process. We also manage group motor coach transportation, food and beverages, entertainment, stage and lighting for group of 10 to 4000.

Target Market(s)

Corporations and associations

Industry/Entity Type

Event Planning

Contact Information for Business Card

standard size 3.5" wide and 2" tall

Font styles to use
Serif
Sans Serif

Colors
f37122
f78f20
333333
5c5c5c
9d9d9d
f68d4d

Requirements
Must have
• {name}
• Velmora Linkway
• P.O. Box 7384, Grand Rapids, M I 49568
• www.velmoralinkway.com
• {email}
• {phone}
• {mobile phone}
Nice to have
• Our colors are black, grey and orange as an accent color
Should not have
• I am not happy with our website layout anymore either. It feels dark and old but it does explain who we are pretty well if you'd like to review; www.velmoralinkway.com

```html
<!DOCTYPE html>
<html lang="en">
<head>
<meta charset="utf-8">
<title>Velmora Linkway — Business Card</title>
<link rel="stylesheet" href="https://fonts.googleapis.com/css2?family=Montserrat:wght@700&family=Roboto:wght@400;500;700&display=swap">
<style>
  :root {
    --orange: #f37122;
    --orange-warm: #ef8623;
    --charcoal: #333333;
    --grey-dark: #5c5c5c;
    --grey: #9d9d9d;
    --ink: #2b2b2b;
    --paper: #ffffff;
    --backdrop: #6e6e6e;
  }
  * { margin: 0; padding: 0; box-sizing: border-box; }
  html, body { width: 1200px; height: 1200px; overflow: hidden; }
  body {
    background: var(--backdrop);
    font-family: "Roboto", Arial, sans-serif;
    position: relative;
  }
  .card {
    position: absolute;
    left: 246px;
    width: 708px;
    box-shadow: 0 6px 14px rgba(0,0,0,0.35);
  }
  /* Front */
  .card-front {
    top: 168px;
    height: 402px;
    background: var(--charcoal);
  }
  .front-mark {
    position: absolute;
    left: 277px; top: 97px;
    width: 154px; height: 154px;
    border-radius: 50%;
    background: var(--orange-warm);
  }
  .front-name {
    position: absolute;
    left: 0; right: 0; top: 255px;
    text-align: center;
    font-family: "Montserrat", Arial, sans-serif;
    font-weight: 700;
    font-size: 26px;
    letter-spacing: 0.5px;
    color: var(--orange-warm);
  }
  /* Back */
  .card-back {
    top: 632px;
    height: 400px;
    background: var(--paper);
    overflow: hidden;
  }
  .back-mark {
    position: absolute;
    left: 256px; top: 36px;
    width: 80px; height: 80px;
    border-radius: 50%;
    background: var(--orange-warm);
  }
  .back-name {
    position: absolute;
    left: 352px; top: 58px;
    font-family: "Montserrat", Arial, sans-serif;
    font-weight: 700;
    font-size: 29px;
    color: var(--grey);
    white-space: nowrap;
  }
  .person {
    position: absolute;
    left: 34px; top: 162px;
  }
  .person-name {
    font-weight: 700;
    font-size: 27px;
    color: var(--orange-warm);
    line-height: 32px;
  }
  .person-title {
    font-size: 18px;
    color: var(--ink);
    line-height: 22px;
  }
  .person-rule {
    position: absolute;
    left: 0; top: 222px;
    width: 251px; height: 2px;
    background: var(--orange-warm);
  }
  .contact-list {
    position: absolute;
    right: 36px; top: 206px;
    list-style: none;
  }
  .contact-list li {
    display: flex;
    justify-content: flex-end;
    align-items: center;
    height: 24px;
    font-size: 18.5px;
    color: var(--ink);
  }
  .contact-list svg {
    width: 20px; height: 20px;
    margin-left: 8px;
    fill: var(--orange-warm);
  }
  .address {
    position: absolute;
    right: 36px; top: 318px;
    text-align: right;
    font-size: 18.5px;
    line-height: 24px;
    color: var(--ink);
  }
  .bottom-band {
    position: absolute;
    left: 0; bottom: 0;
    width: 708px; height: 14px;
  }
</style>
</head>
<body>
  <section class="card card-front" aria-label="Card front">
    <div class="front-mark" aria-hidden="true"></div>
    <div class="front-name">VELMORA LINKWAY</div>
  </section>

  <section class="card card-back" aria-label="Card back">
    <div class="back-mark" aria-hidden="true"></div>
    <div class="back-name">VELMORA LINKWAY</div>

    <div class="person">
      <div class="person-name">Daniel Marsh</div>
      <div class="person-title">Managing Partner</div>
    </div>
    <div class="person-rule"></div>

    <ul class="contact-list">
      <li>00-000-0000
        <svg viewBox="0 0 20 20" aria-hidden="true"><path d="M6 1h8a2 2 0 0 1 2 2v14a2 2 0 0 1-2 2H6a2 2 0 0 1-2-2V3a2 2 0 0 1 2-2zm0 2v11h8V3zm4 12.2a1 1 0 1 0 0 2 1 1 0 0 0 0-2z"/></svg>
      </li>
      <li>00-000-0000
        <svg viewBox="0 0 20 20" aria-hidden="true"><path d="M1 7c2-3 16-3 18 0v2h-4V7.5c-2-.8-8-.8-10 0V9H1zm5 2h8l3 4v5H3v-5zm4 2.5a2 2 0 1 0 0 4 2 2 0 0 0 0-4z"/></svg>
      </li>
      <li>dmarsh@velmoralinkway.com
        <svg viewBox="0 0 20 20" aria-hidden="true"><path d="M1 4h18v12H1zm2 2v.4l7 5 7-5V6zm0 2.8V14h14V8.8l-7 5z"/></svg>
      </li>
      <li>www.velmoralinkway.com
        <svg viewBox="0 0 20 20" aria-hidden="true" fill="none" stroke="#ef8623" stroke-width="1.3" style="fill:none"><circle cx="10" cy="10" r="8.3"/><ellipse cx="10" cy="10" rx="3.6" ry="8.3"/><path d="M1.7 10h16.6M3 5.8h14M3 14.2h14M10 1.7v16.6"/></svg>
      </li>
    </ul>

    <div class="address">
      Velmora Linkway<br>
      P.O. Box 7384, Grand Rapids, M I 49568
    </div>

    <svg class="bottom-band" viewBox="0 0 708 14" preserveAspectRatio="none" aria-hidden="true">
      <polygon points="0,0 440,0 450,14 0,14" fill="var(--orange-warm)"/>
      <polygon points="448,0 708,0 708,14 458,14" fill="var(--charcoal)"/>
    </svg>
  </section>
</body>
</html>
```